IT Company based on Biology Business Needs a Professional Web Design

We need a professional business website design for a new company called 'Vast KELP'. We develop the machine learning solutions especially focused on deep learning algorithms for biology industry. Our initial product is a vision detection on biological images to help doctors diagnose the symptoms. We would like to see designs that use the color green.

Industry/Entity Type

Business

Number of Pages Required

5+ page

```html
<!DOCTYPE html>
<html lang="en">
<head>
<meta charset="utf-8">
<title>Vast KELP — Machine Learning for Biology</title>
<link href="https://fonts.googleapis.com/css2?family=Open+Sans:wght@400;600&display=swap" rel="stylesheet">
<style>
  :root{
    --green:#3aa936;
    --green-bright:#6cc24a;
    --green-deep:#0f8a43;
    --green-band:#2f9e27;
    --dark:#1b1b1b;
    --footer:#1f1f1f;
    --footer-line:#333;
    --text-grey:#8a8a8a;
    --white:#ffffff;
  }
  *{margin:0;padding:0;box-sizing:border-box}
  html,body{width:686px;height:1200px;overflow:hidden;background:var(--white)}
  body{font-family:"Open Sans",Arial,sans-serif;position:relative}
  .abs{position:absolute}

  /* Hero */
  .hero{position:absolute;left:0;top:0;width:686px;height:295px;
    background:radial-gradient(ellipse at 70% 40%,#5a5a5a 0%,#2a2a2a 45%,#111 100%);
    border-top:3px solid var(--green);border-bottom:3px solid var(--green)}
  .logo{left:82px;top:25px;display:flex;align-items:center;gap:5px;color:var(--green-bright);font-weight:600;font-size:13px;letter-spacing:-.2px}
  .logo-dot{width:8px;height:8px;border-radius:50%;background:var(--green-bright)}
  .nav a{position:absolute;top:29px;color:var(--white);font-size:8.5px;text-decoration:none;letter-spacing:.2px}
  .nav a.active{color:var(--green-bright)}
  .search{left:578px;top:22px;width:20px;height:20px;border-radius:50%;background:var(--green-bright)}
  .hero-title{left:82px;top:164px;color:var(--white);font-size:17px;line-height:22px}
  .btn-small{left:82px;top:223px;width:66px;height:16px;background:var(--green-bright);color:var(--white);font-size:6.5px;display:flex;align-items:center;justify-content:center;gap:3px}
  .arrow{top:144px}

  /* Welcome */
  .welcome-title{left:0;width:686px;top:328px;text-align:center;color:var(--green-bright);font-size:16px}
  .welcome-text{left:82px;width:522px;top:366px;text-align:center;color:var(--text-grey);font-size:7px;line-height:11px}
  .btn-contact{left:290px;top:418px;width:106px;height:27px;background:var(--green-deep);color:var(--white);font-size:11px;display:flex;align-items:center;justify-content:center}
  .welcome-deco{left:608px;top:318px;width:56px;height:126px;background:linear-gradient(180deg,#e6f3e3,#eef5f2);opacity:.8;border-radius:4px}

  /* Solutions */
  .solutions{position:absolute;left:0;top:484px;width:686px;height:302px;
    background:radial-gradient(ellipse at 48% 8%,#b6e06a 0%,#5fbd3a 22%,var(--green-band) 55%,#239a1e 100%)}
  .sol-title{left:0;width:686px;top:28px;text-align:center;color:var(--white);font-size:16px}
  .sol-item{width:170px;text-align:center;color:var(--white)}
  .sol-item h3{font-weight:400;font-size:13px;margin-bottom:19px}
  .sol-item p{font-size:7.2px;line-height:11px}
  .sol-icon{top:78px}

  /* Video */
  .video{position:absolute;left:0;top:786px;width:686px;height:260px;
    background:radial-gradient(ellipse at 40% 30%,#4a5563 0%,#2c333d 50%,#1a1d23 100%)}
  .video-text{left:0;width:686px;top:151px;text-align:center;color:var(--white);font-size:14px;line-height:22px}
  .btn-watch{left:296px;top:212px;width:94px;height:20px;background:var(--green-deep);color:var(--white);font-size:8px;display:flex;align-items:center;justify-content:center}

  /* Footer */
  .footer{position:absolute;left:0;top:1046px;width:686px;height:154px;background:var(--footer)}
  .foot-links{list-style:none;top:36px}
  .foot-links li{color:var(--white);font-size:6.5px;line-height:13.6px}
  .newsletter-label{left:350px;top:36px;color:var(--white);font-size:6.5px;display:flex;align-items:center;gap:4px}
  .newsletter{left:350px;top:54px;width:208px;height:18px;border:1px solid #3a3a3a;display:flex}
  .newsletter span{flex:1;color:#777;font-size:5.5px;display:flex;align-items:center;padding-left:7px}
  .newsletter b{width:60px;background:var(--green-bright);color:var(--white);font-size:6px;font-weight:600;display:flex;align-items:center;justify-content:center}
  .bottom-bar{top:116px;left:0;width:686px;height:38px;border-top:1px solid var(--footer-line)}
  .copyright{left:82px;top:14px;color:var(--white);font-size:6.5px}
  .legal{right:82px;top:14px;color:var(--white);font-size:6.5px}
</style>
</head>
<body>

<header class="hero">
  <div class="abs" role="img" aria-label="Black and white DNA double helix with molecular hexagon graphics" style="inset:0"></div>
  <div class="abs logo"><span class="logo-dot"></span>VAST KELP</div>
  <nav class="nav">
    <a class="active" style="left:291px">HOME</a>
    <a style="left:339px">ABOUT US</a>
    <a style="left:402px">SOLUTIONS</a>
    <a style="left:471px">FAQ'S</a>
    <a style="left:517px">CONTACT US</a>
  </nav>
  <div class="abs search">
    <svg width="20" height="20" viewBox="0 0 20 20"><circle cx="9" cy="9" r="3.2" fill="none" stroke="#fff" stroke-width="1.4"/><line x1="11.3" y1="11.3" x2="13.6" y2="13.6" stroke="#fff" stroke-width="1.6"/></svg>
  </div>
  <svg class="abs arrow" style="left:28px" width="12" height="14" viewBox="0 0 12 14"><polyline points="8,2 3,7 8,12" fill="none" stroke="#fff" stroke-width="1.6"/></svg>
  <svg class="abs arrow" style="left:647px" width="12" height="14" viewBox="0 0 12 14"><polyline points="4,2 9,7 4,12" fill="none" stroke="#fff" stroke-width="1.6"/></svg>
  <h1 class="abs hero-title" style="font-weight:400">IT company working<br>on Biology business</h1>
  <div class="abs btn-small">LEARN MORE
    <svg width="7" height="7" viewBox="0 0 8 8"><circle cx="4" cy="4" r="4" fill="#fff"/><polyline points="3,2 5,4 3,6" fill="none" stroke="#6cc24a" stroke-width="1.2"/></svg>
  </div>
</header>

<section>
  <h2 class="abs welcome-title" style="font-weight:400">WELCOME TO VAST KELP</h2>
  <p class="abs welcome-text">Sed ut perspiciatis unde omnis iste natus error sit voluptatem accusantium doloremque laudantium, totam rem aperiam, eaque ipsa quae ab illo inventore veritatis et quasi architecto beatae vitae dicta sunt explicabo. Nemo enim ipsam voluptatem quia voluptas sit aspernatur aut odit aut fugit, sed quia consequuntur magni dolores eos qui ratione voluptatem sequi nesciunt. Neque porro quisquam est, qui dolorem ipsum quia dolor sit amet,</p>
  <div class="abs btn-contact">CONTACT US</div>
  <div class="abs welcome-deco" role="img" aria-label="Faint green DNA strand decoration"></div>
</section>

<section class="solutions">
  <h2 class="abs sol-title" style="font-weight:400">WE DEVELOP THE MACHINE LEARNING SOLUTIONS</h2>

  <svg class="abs sol-icon" style="left:134px" width="60" height="60" viewBox="0 0 60 60" aria-label="Molecule icon">
    <g stroke="#fff" stroke-width="3" fill="#fff">
      <line x1="30" y1="30" x2="12" y2="38"/><line x1="30" y1="30" x2="40" y2="12"/><line x1="30" y1="30" x2="48" y2="34"/><line x1="30" y1="30" x2="36" y2="50"/><line x1="30" y1="30" x2="20" y2="16"/>
      <circle cx="30" cy="30" r="8"/><circle cx="12" cy="38" r="4"/><circle cx="40" cy="12" r="4"/><circle cx="48" cy="34" r="3"/><circle cx="36" cy="50" r="4.5"/><circle cx="20" cy="16" r="3"/>
    </g>
  </svg>
  <svg class="abs sol-icon" style="left:312px;top:74px" width="60" height="64" viewBox="0 0 60 64" aria-label="DNA icon">
    <g fill="none" stroke="#fff" stroke-width="4" stroke-linecap="round">
      <path d="M14 6 C14 26 46 30 46 50"/><path d="M46 6 C46 14 40 20 34 24 M26 36 C20 40 14 46 14 58"/>
    </g>
    <g stroke="#fff" stroke-width="2"><line x1="18" y1="14" x2="44" y2="14"/><line x1="24" y1="22" x2="38" y2="22"/><line x1="22" y1="40" x2="40" y2="40"/><line x1="18" y1="48" x2="44" y2="48"/></g>
  </svg>
  <svg class="abs sol-icon" style="left:492px" width="60" height="60" viewBox="0 0 60 60" aria-label="Lungs icon">
    <g fill="#fff">
      <rect x="28" y="4" width="4" height="22" rx="2"/>
      <path d="M26 20 C16 16 6 30 4 48 C4 54 14 54 26 48 Z"/>
      <path d="M34 20 C44 16 54 30 56 48 C56 54 46 54 34 48 Z"/>
    </g>
  </svg>

  <div class="abs sol-item" style="left:79px;top:170px"><h3>MOLECULAR</h3>
    <p>Sed ut perspiciatis unde omnis iste natus error sit voluptatem accusantium doloremque laudantium, totam rem aperiam, eaque ipsa quae ab illo inventore veritatis et quasi architecto beatae vitae dicta sunt explicabo.</p></div>
  <div class="abs sol-item" style="left:257px;top:166px"><h3 style="margin-bottom:23px">CELLULAR</h3>
    <p>Sed ut perspiciatis unde omnis iste natus error sit voluptatem accusantium doloremque laudantium, totam rem aperiam, eaque ipsa quae ab illo inventore veritatis et quasi architecto beatae vitae dicta sunt explicabo.</p></div>
  <div class="abs sol-item" style="left:437px;top:166px"><h3 style="margin-bottom:23px">ORGANISM</h3>
    <p>Sed ut perspiciatis unde omnis iste natus error sit voluptatem accusantium doloremque laudantium, totam rem aperiam, eaque ipsa quae ab illo inventore veritatis et quasi architecto beatae vitae dicta sunt explicabo.</p></div>
</section>

<section class="video" role="img" aria-label="Blurred microscope in a lab with faint DNA and hexagon graphics">
  <svg class="abs" style="left:320px;top:93px" width="46" height="46" viewBox="0 0 46 46">
    <circle cx="23" cy="23" r="20" fill="none" stroke="rgba(255,255,255,.55)" stroke-width="3"/>
    <polygon points="18,13 33,23 18,33" fill="rgba(255,255,255,.55)"/>
  </svg>
  <p class="abs video-text">Our initial product is a vision detection on biological images to help<br>doctors diagnose the symptoms</p>
  <div class="abs btn-watch">WATCH NOW</div>
</section>

<footer class="footer">
  <ul class="abs foot-links" style="left:82px">
    <li>HOME</li><li>ABOUT US</li><li>SOLUTIONS</li><li>FAQ'S</li><li>CONTACT US</li>
  </ul>
  <ul class="abs foot-links" style="left:215px">
    <li>TERMS &amp; CONDITIONS</li><li>PRIVACY POLICY</li><li>HELP</li><li>COOKIES</li>
  </ul>
  <div class="abs newsletter-label">
    <svg width="7" height="5" viewBox="0 0 7 5"><rect x=".5" y=".5" width="6" height="4" fill="none" stroke="#6cc24a"/><polyline points=".5,.5 3.5,3 6.5,.5" fill="none" stroke="#6cc24a" stroke-width=".8"/></svg>
    SIGN UP FOR NEWSLETTER
  </div>
  <div class="abs newsletter"><span>ENTER YOUR E-MAIL ADDRESS</span><b>SUBSCRIBE</b></div>
  <div class="abs bottom-bar">
    <p class="abs copyright">© 2016 COMPANY NAME | ALL RIGHTS RESERVED</p>
    <p class="abs legal">PRIVACY POLICY &nbsp;| TERMS &amp; CONDITIONS</p>
  </div>
</footer>

</body>
</html>
```